KLV Messaging - veteran and exclusive boutique copywriting agency

PROJECT NEEDS:
1. Website design - full homepage design and inner page top banner design
2. Logo design
* Please see attached Briefs (Word Docs) for descriptions of what is needed for 1 and 2 above.
ABOUT THE CLIENT:
KLV Messaging is a veteran and exclusive boutique copywriting agency run by Marcus Holloway. Marcus is an award-winning published novelist and an accomplished executive ghostwriter with articles regularly published prominent technology publications like Brisk, ByteHarbor, FoundryPulse, and more. For nearly three decades, Marcus has focused solely on the technology sector - serving clients in Israel, Europe and the US.

Target Market(s)

hi-tech companies run by serious, confident professionals.

Industry/Entity Type

Business

Number of Pages Required

2 page

Font styles to use
Sans Serif
Other font styles liked:
• font should be modern

Colors
0054AA
0677BA
7BADD7
CADEEF
E8F1F8
F0912C
F2A743
F7CA91
FBE8D2
FDF5EE

Requirements
Must have
• psd files for logo, homepage design, and inner page top banner design
Nice to have
• Please see attached Website and Logo Design Briefs (Word Docs)
Should not have

```html
<!DOCTYPE html>
<html lang="en">
<head>
<meta charset="utf-8">
<title>KLV Messaging – Creative Copywriter</title>
<link href="https://fonts.googleapis.com/css2?family=Poppins:ital,wght@0,400;0,500;0,600;0,700;0,800;1,400&display=swap" rel="stylesheet">
<style>
  :root{
    --orange:#ffa500;
    --orange-bright:#ffb800;
    --navy:#07079a;
    --navy-soft:#1a1aa6;
    --navy-light:#2525b0;
    --cyan:#00c3cc;
    --ink:#252540;
    --ink-dark:#111122;
    --body-text:#3a3a4e;
    --white:#ffffff;
    --black:#000000;
  }
  *{margin:0;padding:0;box-sizing:border-box}
  html,body{width:1200px;height:3002px;overflow:hidden;background:var(--white)}
  body{position:relative;font-family:'Poppins',sans-serif;color:var(--ink)}

  /* header */
  .site-header{position:absolute;left:0;top:0;width:1200px;height:100px;background:var(--orange);z-index:3}
  .brand{position:absolute;left:117px;top:32px;color:var(--white);font-weight:600;font-size:26px;line-height:36px;letter-spacing:0.5px}
  .main-nav a{position:absolute;top:34px;color:var(--white);font-size:24px;line-height:32px;text-decoration:none;font-weight:400}

  /* hero */
  .hero-art{position:absolute;left:0;top:100px;width:1200px;height:700px;z-index:1}
  .hero-title{position:absolute;left:114px;top:205px;color:var(--white);font-weight:800;font-size:90px;line-height:98px;letter-spacing:1px;z-index:2}
  .hero-copy{position:absolute;left:117px;top:417px;width:560px;color:var(--white);font-size:21px;line-height:28px;z-index:2}
  .hero-copy p + p{margin-top:27px;padding-left:6px}
  .btn{position:absolute;display:flex;align-items:center;justify-content:center;font-weight:600;font-size:17px;color:var(--white);text-decoration:none;border-radius:3px;z-index:2}
  .btn-cyan{background:var(--cyan)}
  .btn-outline{border:2px solid var(--white)}
  .btn-orange{background:var(--orange)}
  .btn-bright{background:var(--orange-bright)}

  /* intro */
  .section-title{position:absolute;left:106px;font-weight:600;font-size:51px;line-height:60px;color:var(--ink)}
  .section-title.dark{color:var(--ink-dark);left:104px}
  .title-bar{position:absolute;height:8px;background:var(--orange)}
  .intro-copy{position:absolute;left:106px;top:946px;width:590px;font-style:italic;font-size:25.5px;line-height:31.5px;color:var(--ink)}
  .intro-copy p + p{margin-top:32px}
  .photo{position:absolute}

  /* services band */
  .services-art{position:absolute;left:0;top:1410px;width:1200px;height:620px}
  .service-card{position:absolute;top:1491px;width:460px;text-align:center;color:var(--white)}
  .service-card .photo-frame{margin:0 auto;width:333px;height:238px;background:var(--white);padding:8px}
  .service-card .photo-fill{width:100%;height:100%;border-radius:8px}
  .service-card h3{margin-top:44px;font-weight:600;font-size:34px;line-height:42px}
  .service-card p{margin:17px auto 0;font-size:21px;line-height:25px}
  .service-card.messaging p{width:420px}
  .service-card.collateral p{width:330px}

  /* success */
  .success-copy{position:absolute;left:106px;top:2216px;width:980px;font-size:24.5px;line-height:35px;color:var(--body-text)}
  .success-copy p + p{margin-top:35px}

  /* footer */
  .site-footer{position:absolute;left:0;top:2870px;width:1200px;height:132px;background:var(--black);color:var(--white)}
  .footer-nav a{position:absolute;top:22px;color:var(--white);font-weight:500;font-size:22px;line-height:30px;text-decoration:none}
  .copyright{position:absolute;left:0;width:1200px;top:92px;text-align:center;font-size:14px;font-weight:500}
</style>
</head>
<body>

<header class="site-header">
  <div class="brand">KLV Messaging</div>
  <nav class="main-nav">
    <a style="left:381px">About</a>
    <a style="left:492px">Services</a>
    <a style="left:632px">Industries</a>
    <a style="left:790px">Portfolio</a>
    <a style="left:928px">Clients</a>
    <a style="left:1050px">Contact</a>
  </nav>
</header>

<svg class="hero-art" viewBox="0 100 1200 700">
  <defs>
    <clipPath id="hero-clip"><path d="M0 100 H1200 V705 Q600 800 0 693 Z"/></clipPath>
    <linearGradient id="portrait-tone" x1="0" y1="0" x2="0" y2="1">
      <stop offset="0" stop-color="#3a3d47"/>
      <stop offset="0.45" stop-color="#6b7383"/>
      <stop offset="0.7" stop-color="#8fb0d6"/>
      <stop offset="1" stop-color="#a9c6e6"/>
    </linearGradient>
  </defs>
  <g clip-path="url(#hero-clip)">
    <rect x="0" y="100" width="1200" height="700" fill="var(--navy)"/>
    <circle cx="70" cy="180" r="180" fill="var(--navy-soft)"/>
    <circle cx="10" cy="640" r="85" fill="var(--navy-soft)"/>
    <circle cx="38" cy="555" r="38" fill="var(--navy-light)"/>
    <circle cx="1002" cy="501" r="309" fill="url(#portrait-tone)" role="img" aria-label="Studio portrait of the copywriter in a light blue shirt against a dark grey backdrop"/>
  </g>
</svg>

<h1 class="hero-title">CREATIVE<br>COPYWRITER</h1>
<div class="hero-copy">
  <p>Your messages must be compelling in a crowded market. Your offering must stand out from the competition.however, not by yelling.</p>
  <p>It is not a speech; it is a discussion.</p>
</div>
<a class="btn btn-cyan" style="left:118px;top:614px;width:151px;height:57px">Contact Us</a>
<a class="btn btn-outline" style="left:298px;top:614px;width:152px;height:57px">Our Service</a>

<h2 class="section-title" style="top:846px">Giving Voice to Your Vision</h2>
<div class="title-bar" style="left:106px;top:911px;width:122px"></div>
<div class="intro-copy">
  <p>Blog posts that are interesting and make sure your business is always in the conversation. Informational, educational, entertaining, and engaging white papers and ebooks.</p>
  <p>Your skills should be shared through content marketing. It involves demonstrating to the world not only what you know, but also how well you can articulate that knowledge.</p>
</div>
<div class="photo" style="left:719px;top:967px;width:417px;height:297px;background:linear-gradient(160deg,#a9c8dd 0%,#d9e4ea 45%,#b98a66 100%);border-radius:10px" role="img" aria-label="Child in a bucket hat fishing at the water's edge"></div>
<a class="btn btn-orange" style="left:106px;top:1276px;width:151px;height:57px">Our Service</a>

<svg class="services-art" viewBox="0 1410 1200 620" aria-hidden="true">
  <defs><clipPath id="band-clip"><path d="M0 1410 H1200 V1981 Q600 2077 0 1981 Z"/></clipPath></defs>
  <g clip-path="url(#band-clip)">
    <rect x="0" y="1410" width="1200" height="620" fill="var(--navy)"/>
    <circle cx="20" cy="1400" r="120" fill="var(--navy-soft)"/>
    <circle cx="480" cy="1600" r="65" fill="var(--navy-soft)"/>
    <circle cx="520" cy="1538" r="25" fill="var(--navy-light)"/>
    <circle cx="830" cy="1720" r="185" fill="var(--navy-soft)"/>
    <circle cx="674" cy="1805" r="40" fill="var(--navy-light)"/>
    <circle cx="1078" cy="1545" r="60" fill="var(--navy-light)"/>
    <circle cx="1200" cy="1765" r="220" fill="var(--navy-soft)"/>
    <circle cx="140" cy="2030" r="165" fill="var(--navy-soft)"/>
  </g>
</svg>

<div class="service-card messaging" style="left:89px">
  <div class="photo-frame"><div class="photo-fill" style="background:linear-gradient(120deg,#5a6e55 0%,#dfe8ea 50%,#6fbd63 100%)" role="img" aria-label="Child in a hat looking through a telescope"></div></div>
  <h3>Messaging</h3>
  <p>The importance of well defined, precisely targeted, and well-conceived corporate communications is obvious in a crowded market.</p>
</div>
<div class="service-card collateral" style="left:654px">
  <div class="photo-frame"><div class="photo-fill" style="background:linear-gradient(150deg,#3c3f3a 0%,#5a5c55 60%,#8a6a4a 100%)" role="img" aria-label="Child writing letters on a chalkboard"></div></div>
  <h3>Collateral</h3>
  <p>Marketing collateral that effectively communicates who you are and what you want to say.</p>
</div>

<h2 class="section-title dark" style="top:2105px">Redefining Your Success</h2>
<div class="title-bar" style="left:106px;top:2170px;width:111px"></div>
<div class="success-copy">
  <p>KLV Messaging offers a package of consulting services, organized brainstorming sessions and workshops, and usable deliverables - all tailored to your specific needs and timeframe. The company has a refined messaging methodology that has already been applied in businesses across diverse sectors and at various lifecycle stages.</p>
  <p>In order to comprehend, contrast, hone, and define your marketing messages and positioning, we engage closely with the important decision-makers in your organization. We provide a fresh perspective on who you are and what you do by leveraging your experience and industry expertise, combined with a custom-defined scope of independent market research.</p>
  <p>As a result, all of your marketing materials will be built on clearer, more targeted marketing messages that are presented in an approachable way.</p>
</div>
<a class="btn btn-bright" style="left:105px;top:2752px;width:151px;height:57px">Our Service</a>

<footer class="site-footer">
  <nav class="footer-nav">
    <a style="left:367px">About</a>
    <a style="left:472px">Services</a>
    <a style="left:614px">Portfolio</a>
    <a style="left:749px">Contact</a>
  </nav>
  <div class="copyright">Copyright © 2023 KLV Messaging</div>
</footer>

</body>
</html>
```